Poster Board Design

Hello.
This is what we will need on the design
Photo of truck
Company logo
Website: Bluerivoxfreightlines.com

Train Here... Drive here
$2,600 Weekly Average
Text/ Call: 428-555-7302
Must fit poster board size of 10'5"x 22'8"

i sent it via email reply idk how to send the photo in this box

```html
<!DOCTYPE html>
<html lang="en">
<head>
<meta charset="utf-8">
<title>Bluerivox Freightlines – Poster Board</title>
<link rel="stylesheet" href="https://fonts.googleapis.com/css2?family=Montserrat:ital,wght@0,400;0,700;0,800;1,900&display=swap">
<style>
  :root {
    --navy: #13264f;
    --navy-light: #3d67a6;
    --red: #e0291b;
    --red-dark: #b3231a;
    --maroon: #6b1410;
    --white: #ffffff;
    --ink: #2c2c34;
    --backdrop: #bdbdbd;
  }
  * { margin: 0; padding: 0; box-sizing: border-box; }
  html, body { width: 1036px; height: 1200px; overflow: hidden; }
  body {
    background: var(--backdrop);
    font-family: "Montserrat", Arial, sans-serif;
    position: relative;
  }
  .poster {
    position: absolute;
    left: 18px;
    top: 370px;
    width: 1000px;
    height: 460px;
    background: var(--white);
    overflow: hidden;
  }
  .poster-shapes { position: absolute; inset: 0; }
  .headline {
    position: absolute;
    font-style: italic;
    font-weight: 900;
    line-height: 1;
    letter-spacing: -1px;
    white-space: nowrap;
  }
  .headline--train { left: 57px; top: 30px; font-size: 66px; color: var(--white); }
  .headline--drive {
    left: 144px; top: 96px; font-size: 66px; color: var(--red);
    -webkit-text-stroke: 2px var(--white);
    paint-order: stroke fill;
  }
  .pay-amount {
    position: absolute;
    left: 232px; top: 174px;
    font-size: 72px; font-weight: 800; line-height: 1;
    color: var(--white);
    letter-spacing: -2px;
    -webkit-text-stroke: 6px var(--maroon);
    paint-order: stroke fill;
  }
  .pay-label {
    position: absolute;
    left: 492px; top: 178px; width: 205px; height: 66px;
    background: var(--red);
    color: var(--white);
    font-weight: 800; font-size: 26px; line-height: 30px;
    padding: 4px 0 0 28px;
  }
  .contact-tag {
    position: absolute;
    left: 222px; top: 297px; width: 223px; height: 33px;
    background: var(--red-dark);
    color: var(--white);
    font-weight: 700; font-size: 21px;
    text-align: center; line-height: 33px;
  }
  .contact-line {
    position: absolute;
    left: 127px;
    display: flex; align-items: center; gap: 15px;
    color: var(--ink); font-weight: 800; white-space: nowrap;
  }
  .contact-line--phone { top: 343px; font-size: 50px; letter-spacing: -0.5px; }
  .contact-line--web { top: 402px; font-size: 28px; }
  .contact-icon { width: 37px; height: 37px; flex: none; }
  .divider {
    position: absolute; left: 628px; top: 320px;
    width: 2px; height: 122px; background: var(--red);
  }
  .brand-name {
    position: absolute; left: 672px; top: 340px;
    color: var(--ink); font-weight: 400; font-size: 24px;
    line-height: 28px; letter-spacing: 1px;
  }
</style>
</head>
<body>
  <main class="poster">
    <svg class="poster-shapes" viewBox="0 0 1000 460" width="1000" height="460">
      <defs>
        <linearGradient id="skyFill" x1="0" y1="0" x2="1" y2="0.4">
          <stop offset="0" stop-color="#13264f"/>
          <stop offset="0.55" stop-color="#24457c"/>
          <stop offset="1" stop-color="#4f7fbe"/>
        </linearGradient>
        <linearGradient id="truckFill" x1="0" y1="0" x2="0" y2="1">
          <stop offset="0" stop-color="#6f95c8" stop-opacity="0"/>
          <stop offset="0.35" stop-color="#a7b0bb"/>
          <stop offset="0.8" stop-color="#8d939b"/>
          <stop offset="1" stop-color="#d8d6d0"/>
        </linearGradient>
      </defs>
      <polygon points="0,0 1000,0 1000,268 700,296 0,176" fill="url(#skyFill)"/>
      <polygon points="0,176 700,296 240,263 0,255" fill="var(--red)"/>
      <polygon points="0,255 240,263 0,424" fill="var(--red-dark)"/>
      <polygon points="640,40 1000,40 1000,268 700,296 640,280" fill="url(#truckFill)"
               role="img" aria-label="Photo of a silver semi truck on the road under a blue sky"/>
    </svg>

    <div class="headline headline--train">TRAIN HERE...</div>
    <div class="headline headline--drive">DRIVE HERE</div>

    <div class="pay-amount">$2,600</div>
    <div class="pay-label">WEEKLY<br>AVERAGE</div>

    <div class="contact-tag">Text/ Call:</div>
    <div class="contact-line contact-line--phone">
      <svg class="contact-icon" viewBox="0 0 36 36" aria-hidden="true">
        <circle cx="18" cy="18" r="18" fill="var(--red-dark)"/>
        <path d="M12 9c1 0 3 4 3 5s-2 2-2 3 4 6 6 6 2-2 3-2 5 2 5 3-2 4-4 4C15 28 8 21 8 13c0-2 3-4 4-4z" fill="var(--white)"/>
      </svg>
      <span>428-555-7302</span>
    </div>
    <div class="contact-line contact-line--web">
      <svg class="contact-icon" viewBox="0 0 36 36" aria-hidden="true">
        <circle cx="18" cy="18" r="18" fill="var(--red-dark)"/>
        <g fill="none" stroke="var(--white)" stroke-width="1.6">
          <circle cx="18" cy="18" r="9"/>
          <ellipse cx="18" cy="18" rx="4" ry="9"/>
          <line x1="9" y1="18" x2="27" y2="18"/>
          <line x1="11" y1="13" x2="25" y2="13"/>
          <line x1="11" y1="23" x2="25" y2="23"/>
        </g>
      </svg>
      <span>Bluerivoxfreightlines.com</span>
    </div>

    <div class="divider"></div>
    <div class="brand-name">BLUERIVOX<br>FREIGHTLINES</div>
  </main>
</body>
</html>
```